Unique Elegant Stationary Set

Prepare a unique eye catching stationary set consisting of :
(1) Letterhead
(2) A3 Envelope
(3) Business Card
(4) Email Signature Banner

Package to be elegant, modern, and designers not only to think of design or colors but also materials could make a big difference, embossing, debossing, glossy, matt ....etc.

I attached both our new logos (Stacked or Linear) noting you may use any of them but you cant modify anything in the logos. Also attached our final draft portfolio to see what type of projects we work on and i also have here a glimboard page link showing the direction we want: https://www.glimboard.example/ravelkoton/business-card-design/

Target Market(s)

VVIP / Elite Developers

Industry/Entity Type

Architecture

Font styles to use
Sans Serif
Other font styles liked:
• unitext

Requirements
Should not have
• too many colors, or being busy in general. We want something pleasing to the eye

```html
<!DOCTYPE html>
<html lang="en">
<head>
<meta charset="utf-8">
<title>Korvel Studio Stationery Set</title>
<link href="https://fonts.googleapis.com/css2?family=Figtree:wght@400;500;700;800&display=swap" rel="stylesheet">
<style>
  :root {
    --backdrop: #b3b3b3;
    --paper: #ffffff;
    --ink: #111111;
    --card: #000000;
    --brand-red: #c5202a;
    --ghost: #141414;
    --muted: #777777;
    --shadow: 6px 8px 10px rgba(0,0,0,.35);
  }
  * { box-sizing: border-box; margin: 0; padding: 0; }
  html, body { width: 940px; height: 1200px; overflow: hidden; }
  body { background: var(--backdrop); font-family: "Figtree", sans-serif; color: var(--ink); position: relative; }
  .piece { position: absolute; box-shadow: var(--shadow); overflow: hidden; }
  .accent { position: absolute; inset: 0; width: 100%; height: 100%; }
  .accent polygon { fill: var(--brand-red); }

  .wordmark { font-weight: 800; line-height: .9; letter-spacing: 1px; text-transform: uppercase; }
  .wordmark span { display: block; }
  .wordmark .sub { font-size: .32em; letter-spacing: .55em; margin-top: 6px; }

  .contact-list { list-style: none; }
  .contact-list li { display: flex; align-items: center; gap: 7px; line-height: 1.5; }
  .contact-list svg { width: 1em; height: 1em; fill: currentColor; flex: none; }

  /* envelope */
  .envelope { left: 47px; top: 42px; width: 514px; height: 362px; background: var(--paper); }
  .envelope .wordmark { position: absolute; left: 40px; top: 36px; font-size: 48px; color: var(--ink); }
  .envelope .contact-list { position: absolute; left: 340px; top: 46px; font-size: 12.5px; }

  /* business cards */
  .card { width: 295px; height: 167px; background: var(--card); }
  .card-front { left: 586px; top: 42px; color: #fff; }
  .card-front .wordmark { position: absolute; right: 20px; top: 22px; font-size: 34px; color: var(--brand-red); text-align: right; }
  .card-front .person { position: absolute; left: 20px; top: 84px; font-size: 14px; font-weight: 700; }
  .card-front .contact-list { position: absolute; left: 20px; top: 114px; font-size: 8.5px; }
  .card-back { left: 586px; top: 237px; display: flex; align-items: center; justify-content: center; }
  .card-back .wordmark { font-size: 62px; color: var(--ghost); text-align: center; }

  /* letterhead */
  .letterhead { left: 47px; top: 432px; width: 514px; height: 726px; background: var(--paper); }
  .letterhead .wordmark-linear { position: absolute; left: 88px; top: 40px; font-size: 40px; font-weight: 800; color: var(--brand-red); letter-spacing: 1px; }
  .letterhead .contact-list { position: absolute; left: 40px; top: 656px; font-size: 14px; }

  /* email signature */
  .signature { left: 229px; top: 763px; width: 664px; height: 153px; background: var(--card); color: #fff; }
  .signature .wordmark { position: absolute; left: 56px; top: 34px; font-size: 54px; color: var(--brand-red); }
  .signature .divider { position: absolute; left: 356px; top: 36px; width: 1px; height: 82px; background: #4a4a4a; }
  .signature .person { position: absolute; left: 440px; top: 30px; font-size: 20px; font-weight: 700; }
  .signature .contact-list { position: absolute; left: 440px; top: 73px; font-size: 12.5px; }
</style>
</head>
<body>
<svg width="0" height="0" style="position:absolute" aria-hidden="true">
  <defs>
    <symbol id="icon-phone" viewBox="0 0 16 16"><path d="M3.6 1.5l2.2 2.6-1.3 1.6c.8 2 2.3 3.5 4.3 4.4l1.6-1.3 2.6 2.2-1.3 2.3C7 13.3 2.7 9 1.3 2.8z"/></symbol>
    <symbol id="icon-mail" viewBox="0 0 16 16"><path d="M1 3h14v10H1zM2.5 4.5v.4L8 8.6l5.5-3.7v-.4z"/></symbol>
    <symbol id="icon-globe" viewBox="0 0 16 16"><path d="M8 1a7 7 0 100 14A7 7 0 008 1zm0 1.5c.9 0 1.8 1.8 2.1 4.3H5.9C6.2 4.3 7.1 2.5 8 2.5zM2.6 8.2h1.9c.1 1.9.5 3.5 1.1 4.6a5.6 5.6 0 01-3-4.6zm3.3 0h4.2C10 10.8 9 13.5 8 13.5s-2-2.7-2.1-5.3zm5.6 0h1.9a5.6 5.6 0 01-3 4.6c.6-1.1 1-2.7 1.1-4.6zm0-1.4c-.1-1.8-.5-3.4-1.1-4.5a5.6 5.6 0 013 4.5zm-7 0H2.6a5.6 5.6 0 013-4.5c-.6 1.1-1 2.7-1.1 4.5z"/></symbol>
  </defs>
</svg>

<section class="piece envelope" aria-label="Envelope">
  <svg class="accent" viewBox="0 0 525 370" preserveAspectRatio="none" aria-hidden="true">
    <polygon points="0,327 92,327 127,350 382,350 525,281 525,370 132,370 72,344 0,344"/>
  </svg>
  <div class="wordmark"><span>Korvel</span><span class="sub">Studio</span></div>
  <ul class="contact-list">
    <li><svg><use href="#icon-phone"/></svg>+43 123 456 7890</li>
    <li><svg><use href="#icon-mail"/></svg>email@domain.com</li>
    <li><svg><use href="#icon-globe"/></svg>www.korvelstudio.com</li>
  </ul>
</section>

<section class="piece card card-front" aria-label="Business card front">
  <div class="wordmark"><span>Korvel</span><span class="sub">Studio</span></div>
  <p class="person">Your Name</p>
  <ul class="contact-list">
    <li><svg><use href="#icon-phone"/></svg>+43 123 456 7890</li>
    <li><svg><use href="#icon-mail"/></svg>email@domain.com</li>
    <li><svg><use href="#icon-globe"/></svg>www.korvelstudio.com</li>
  </ul>
</section>

<section class="piece card card-back" aria-label="Business card back">
  <div class="wordmark"><span>Korvel</span><span class="sub">Studio</span></div>
</section>

<section class="piece letterhead" aria-label="Letterhead">
  <svg class="accent" viewBox="0 0 525 742" preserveAspectRatio="none" aria-hidden="true">
    <polygon points="504,494 525,494 525,742 417,742 417,719 285,719 285,706 457,706 470,719 504,719"/>
  </svg>
  <p class="wordmark-linear">KORVEL STUDIO</p>
  <ul class="contact-list">
    <li><svg><use href="#icon-phone"/></svg>+43 123 456 7890</li>
    <li><svg><use href="#icon-mail"/></svg>email@domain.com</li>
    <li><svg><use href="#icon-globe"/></svg>www.korvelstudio.com</li>
  </ul>
</section>

<section class="piece signature" aria-label="Email signature banner">
  <div class="wordmark"><span>Korvel</span><span class="sub">Studio</span></div>
  <div class="divider"></div>
  <p class="person">Your Name</p>
  <ul class="contact-list">
    <li><svg><use href="#icon-phone"/></svg>+43 123 456 7890</li>
    <li><svg><use href="#icon-mail"/></svg>email@domain.com</li>
    <li><svg><use href="#icon-globe"/></svg>www.korvelstudio.com</li>
  </ul>
</section>
</body>
</html>
```